Webpage layout and company logo combination

We are trying to renovate an existing site to make it sharper and sophisticated in appearance. This is the existing site: http://www.kestrelhomesnj.com/agents.html . The new presentation should be bright, sharp, sophisticated and should incorporate two additional menu tabs. The menu tabs will be revised as follows: Property Listings, Property Management, Advisory & Consulting, Local Info, R/E Tools, Our Team (please disregard Korean language characters, which will be installed after English version is completed, separately).

It Company

```html
<!DOCTYPE html>
<html lang="en">
<head>
<meta charset="utf-8">
<title>Kestrel Homes</title>
<link href="https://fonts.googleapis.com/css2?family=Oxygen:wght@400;700&display=swap" rel="stylesheet">
<style>
:root{
  --header-bg:#c9cd9b;
  --olive-light:#6f6c3f;
  --olive-dark:#3d381b;
  --nav-top:#6c6a3b;
  --nav-bottom:#4b4724;
  --brand:#6b2a3a;
  --title:#4a4a22;
  --text:#333;
  --muted:#777;
  --line:#dcdcd4;
  --white:#fff;
  --photo-hero:#8ea77a;
  --photo-home:#8a8f6e;
  --photo-tower:#4aa3d3;
  --photo-desk:#d8cbc2;
  --photo-deal-1:#9aab86;
  --photo-deal-2:#a8a08a;
  --photo-deal-3:#a9b6b8;
  --photo-person-1:#7a6f6a;
  --photo-person-2:#9a9c8a;
  --photo-person-3:#8a7468;
}
*{margin:0;padding:0;box-sizing:border-box}
html,body{width:891px;height:1200px;overflow:hidden;background:var(--white)}
body{position:relative;font-family:'Oxygen',sans-serif;color:var(--text)}
.abs{position:absolute}
.header{left:0;top:0;width:891px;height:80px;background:var(--header-bg)}
.brand{left:86px;top:26px;display:flex;align-items:center;gap:8px;font-size:24px;font-weight:700;color:var(--brand);letter-spacing:.5px}
.brand-mark{width:22px;height:22px;border-radius:50%;background:var(--brand)}
.lang{left:720px;top:10px;width:80px;height:23px;border:1px solid #b3b585;background:#e4e6c6;font-size:10px;display:flex;align-items:center;padding-left:8px;gap:6px;color:#333}
.flag{width:15px;height:10px;background:#2d3f7c;border:1px solid #fff}
.phone{left:668px;top:43px;font-size:18px;color:#222;display:flex;align-items:center;gap:5px}
.nav{left:0;top:80px;width:891px;height:36px;background:linear-gradient(var(--nav-top),var(--nav-bottom));border-top:1px solid #e8eacb}
.nav ul{list-style:none;display:flex;position:absolute;left:86px;top:0;height:36px}
.nav li{color:var(--white);font-size:12px;padding:0 14px;line-height:36px;border-right:1px solid #3a3618}
.nav li:first-child{padding-left:16px}
.nav li:last-child{border-right:none}
.hero{left:0;top:116px;width:891px;height:330px;background:linear-gradient(var(--olive-light),var(--olive-dark))}
.hero h1{position:absolute;left:86px;top:82px;color:var(--white);font-weight:400;line-height:1.3}
.hero h1 .l1{display:block;font-size:26.5px}
.hero h1 .l2{display:block;font-size:31px}
.hero p{position:absolute;left:86px;top:158px;width:298px;font-size:8.5px;line-height:15px;color:#ddd9bf}
.dots{position:absolute;left:86px;top:200px;display:flex;gap:3px}
.dots span{width:10px;height:10px;border-radius:50%;background:#8a8760}
.hero-frame{left:424px;top:150px;width:379px;height:245px}
.cards .card{position:absolute;top:465px;width:233px;height:190px;border:1px solid var(--line);background:linear-gradient(#fff 80%,#f3f3f0);box-shadow:0 1px 2px rgba(0,0,0,.08)}
.card .ph{position:absolute;left:10px;top:10px;width:214px;height:99px}
.card h3{position:absolute;left:16px;top:118px;font-size:17px;font-weight:400;color:var(--title)}
.card p{position:absolute;left:16px;top:141px;width:190px;font-size:9.5px;line-height:14px;color:#555}
h2.sec{position:absolute;font-weight:400;color:var(--title);font-size:21px}
.about p{position:absolute;left:85px;width:305px;font-size:9.5px;line-height:15.5px;color:var(--muted)}
.about p.lead{color:var(--text);font-size:10px}
.deal{position:absolute;top:725px;width:126px}
.deal .ph{height:84px}
.deal h4{font-size:11px;font-weight:400;color:#222;margin:7px 0 0 2px}
.deal p{font-size:8.5px;line-height:13px;color:var(--muted);margin:3px 0 0 2px}
.divider{left:85px;top:899px;width:723px;height:1px;background:var(--line)}
.agent{position:absolute;top:954px}
.agent .ph{width:89px;height:83px}
.agent dl{position:absolute;left:101px;top:-1px;width:160px;font-size:10.5px;line-height:17.6px;color:#444}
.agent dt{color:#222}
.footer{left:0;top:1089px;width:891px;height:111px;background:linear-gradient(#5a5530,#3b3619);border-top:1px solid #8a865e}
.footer nav{position:absolute;left:88px;top:25px;font-size:11px;color:var(--white);font-weight:700}
.footer nav span{margin:0 6px;font-weight:400}
.footer small{position:absolute;left:88px;top:49px;font-size:8px;color:#ddd}
.social{position:absolute;left:744px;top:24px;display:flex;gap:7px}
.social span{width:16px;height:16px;border-radius:50%;background:var(--white)}
</style>
</head>
<body>
<header class="abs header">
  <div class="abs brand"><span class="brand-mark"></span>KESTREL HOMES</div>
  <div class="abs lang"><span class="flag"></span>English ▾</div>
  <div class="abs phone">
    <svg width="16" height="16" viewBox="0 0 24 24"><path fill="#222" d="M6.6 10.8a15 15 0 0 0 6.6 6.6l2.2-2.2c.3-.3.7-.4 1-.2 1.1.4 2.3.6 3.6.6.6 0 1 .4 1 1V20c0 .6-.4 1-1 1A17 17 0 0 1 3 4c0-.6.4-1 1-1h3.5c.6 0 1 .4 1 1 0 1.3.2 2.5.6 3.6.1.3 0 .7-.2 1z"/></svg>
    (201) 555-0148
  </div>
</header>

<nav class="abs nav">
  <ul>
    <li>Home</li><li>Property Listings</li><li>Property Management</li><li>Advisory &amp; Consulting</li><li>Local Info</li><li>R/E Tools</li><li>Our Team</li>
  </ul>
</nav>

<section class="abs hero">
  <h1><span class="l1">Aliquam necerat at purus</span><span class="l2">Donec dictum lectus</span></h1>
  <p>Etiam eu urna Sed porta Suspendisse quam leo molestie sed luctus quis feugiat in pede Fusce tellus Sed metus augue convallis</p>
  <div class="dots"><span></span><span></span><span></span><span></span></div>
</section>
<svg class="abs hero-frame" viewBox="0 0 379 245" role="img" aria-label="Photo of suburban houses on a green lawn under a blue sky">
  <path d="M8 0H371Q379 0 379 8V218Q190 195 0 222V8Q0 0 8 0Z" fill="#fff"/>
  <path d="M10 6H368Q373 6 373 11V212Q190 190 6 216V11Q6 6 10 6Z" fill="var(--photo-hero)"/>
</svg>

<div class="cards">
  <article class="card" style="left:85px">
    <div class="ph" role="img" aria-label="Photo of a house porch with flowering shrubs" style="background:var(--photo-home)"></div>
    <h3>Residential Property</h3>
    <p>Morbi diam mauris viverra in gravida eu mattis in ante Morbi eget arcu.</p>
  </article>
  <article class="card" style="left:330px">
    <div class="ph" role="img" aria-label="Photo of glass office towers against the sky" style="background:var(--photo-tower)"></div>
    <h3>Commercial Property</h3>
    <p>Morbi diam mauris viverra in gravida eu mattis in ante Morbi eget arcu.</p>
  </article>
  <article class="card" style="left:576px">
    <div class="ph" role="img" aria-label="Photo of a hand with pen beside a calculator" style="background:var(--photo-desk)"></div>
    <h3>Mortgage Calculator</h3>
    <p>Morbi diam mauris viverra in gravida eu mattis in ante Morbi eget arcu.</p>
  </article>
</div>

<section class="about">
  <h2 class="sec" style="left:85px;top:692px">About Our Company</h2>
  <p class="lead" style="top:724px">Pellentesque faucibus Ut accumsan ultricies elit Maecenas at justo id velit placerat molestie Donec dictum lectus</p>
  <p style="top:759px">Aliquam nec erat at purus cursus interdumVestibulum ligula augue bibendum accumsan vestibulum ut commodo a mi Morbi ornare gravida elit Integer congue augue et malesuada iaculis ipsum dui aliquet felis at cursus magna nisl nec elit</p>
  <p style="top:825px">Vestibulum gravida Praesent elementum elit at tellus Malesuada nec ultricies sit amet porttitor</p>
</section>

<section>
  <h2 class="sec" style="left:424px;top:692px">Featured Deals</h2>
  <div class="deal" style="left:425px">
    <div class="ph" role="img" aria-label="Photo of a house with a sold sign on the lawn" style="background:var(--photo-deal-1)"></div>
    <h4>Property Tittle</h4>
    <p>Morbi ornare gravida elit Integer congue augue et mal esuada iaculis ipsum</p>
  </div>
  <div class="deal" style="left:554px">
    <div class="ph" role="img" aria-label="Photo of a two-storey house with garage" style="background:var(--photo-deal-2)"></div>
    <h4>Property Tittle</h4>
    <p>Morbi ornare gravida elit Integer congue augue et mal esuada iaculis ipsum</p>
  </div>
  <div class="deal" style="left:683px">
    <div class="ph" role="img" aria-label="Photo of a white colonial house" style="background:var(--photo-deal-3)"></div>
    <h4>Property Tittle</h4>
    <p>Morbi ornare gravida elit Integer congue augue et mal esuada iaculis ipsum</p>
  </div>
</section>

<div class="abs divider"></div>

<section>
  <h2 class="sec" style="left:83px;top:920px;color:#222;font-size:19px">Our Agent</h2>
  <div class="agent" style="left:86px">
    <div class="ph" role="img" aria-label="Portrait of the broker seated at a desk" style="background:var(--photo-person-1)"></div>
    <dl><dt>MARTIN KESTREL</dt><dd>Broker/Owner</dd><dd>Direct: 866-555-0193</dd><dd>Office: 201-555-0148</dd><dd>Cell: 201-555-0172</dd></dl>
  </div>
  <div class="agent" style="left:340px">
    <div class="ph" role="img" aria-label="Portrait of a sales agent" style="background:var(--photo-person-2)"></div>
    <dl><dt>Leo Varga</dt><dd>Sales Agent</dd><dd>Direct: 866-555-0193</dd><dd>Office: 201-555-0148</dd><dd>Cell: 201-555-0172</dd></dl>
  </div>
  <div class="agent" style="left:599px">
    <div class="ph" role="img" aria-label="Portrait of a sales agent" style="background:var(--photo-person-3)"></div>
    <dl><dt>Nadia Orlov</dt><dd>Sales Agent</dd><dd>Direct: 866-555-0193</dd><dd>Office: 201-555-0148</dd><dd>Cell: 201-555-0172</dd></dl>
  </div>
</section>

<footer class="abs footer">
  <nav>Home<span>|</span>Property Listings<span>|</span>Property Management<span>|</span>Advisory &amp; Consulting<span>|</span>Local Info<span>|</span>R/E Tools<span>|</span>Our Team</nav>
  <small>© 2013 Company Name.&nbsp; All right reserved.&nbsp; Term of Use</small>
  <div class="social" aria-label="Social links"><span></span><span></span><span></span></div>
</footer>
</body>
</html>
```